A4 Client Referral Program Flyer for Property Management Agency

Harbourleaf Estates Agency is a property management specialist based on Sydney's Northern Beaches in Australia.

We manage mid to high-end rental properties for investors and property owners.
We are currently looking to build our portfolio and are offering existing clients and contacts a referral incentive. We want to sign up more properties to manage.

We are offering the referrer a $250 referral fee and the new owner 2 months of free management to entice them to use Harbourleaf Estates Agency.

We want an A4 Flyer to print and add to other document packages we hand out to clients and suppliers.
If at all possible a matching digital banner would be great too! 1000px wide x 250px

Please find copy attached in Word Doc and our logo attached also.

Please see our website for any more details on our business.

We must be able to have an editable photoshop version (PSD) of the document as well as a print ready PDF version incl any bleed necessary for A4 printing.

Target Market(s)

30-60YO Male and Female

Industry/Entity Type

Real Estate

Font styles to use
Sans Serif

Requirements
Must have
• Company Logo, contact details and copy provided

```html
<!DOCTYPE html>
<html lang="en">
<head>
<meta charset="utf-8">
<title>Harbourleaf Estates Agency – Referral Program Flyer</title>
<link rel="stylesheet" href="https://fonts.googleapis.com/css2?family=Montserrat:wght@400;600;700;800&family=Open+Sans:wght@400;600&display=swap">
<style>
  :root {
    --teal: #4d9ba3;
    --teal-dark: #2f7c86;
    --ink: #1e2529;
    --paper: #ffffff;
    --backdrop: #c9c9c9;
    --muted: #555d61;
  }
  * { box-sizing: border-box; margin: 0; padding: 0; }
  html, body { width: 1185px; height: 1200px; overflow: hidden; background: var(--backdrop); }
  .flyer {
    position: absolute; left: 190px; top: 30px;
    width: 806px; height: 1140px;
    background: var(--paper);
    overflow: hidden;
    font-family: "Montserrat", sans-serif;
    color: var(--ink);
  }
  .brand {
    position: absolute; right: 46px; top: 58px;
    display: flex; align-items: center; gap: 10px;
  }
  .brand-mark { width: 16px; height: 16px; background: var(--teal); }
  .brand-name {
    font-weight: 700; font-size: 22px; letter-spacing: 0.5px;
    color: var(--ink); text-transform: uppercase;
  }
  .hero-photo {
    position: absolute; left: 0; top: 150px; width: 806px; height: 490px;
    clip-path: polygon(0 50px, 100% 0, 100% 100%, 0 100%);
    background: linear-gradient(180deg, #3ea3d6 0%, #7cc3e6 30%, #4a6b5a 55%, #2f5a33 80%, #cfcfc8 100%);
  }
  .header-stripes { position: absolute; left: 0; top: 0; width: 806px; height: 240px; }
  .gallery-line { position: absolute; left: 0; top: 440px; width: 806px; height: 260px; }
  .thumb {
    position: absolute; border: 4px solid var(--teal); background: var(--paper); padding: 4px;
    box-shadow: 0 4px 10px rgba(0,0,0,0.25);
  }
  .thumb-fill { width: 100%; height: 100%; }
  .thumb--exterior { left: 150px; top: 585px; width: 215px; height: 145px; }
  .thumb--exterior .thumb-fill { background: linear-gradient(160deg, #6f9fc4, #d9d6cf 55%, #6b7a6a); }
  .thumb--living { left: 380px; top: 520px; width: 225px; height: 140px; }
  .thumb--living .thumb-fill { background: linear-gradient(160deg, #f1f0ec, #dcd7cc 60%, #c2a77f); }
  .thumb--kitchen { left: 610px; top: 455px; width: 180px; height: 130px; }
  .thumb--kitchen .thumb-fill { background: linear-gradient(160deg, #f5f5f3, #e8e8e4 50%, #b6c95a 75%, #d8d8d6); }
  .headline {
    position: absolute; left: 40px; top: 768px;
    font-weight: 800; font-size: 45px; color: var(--teal); letter-spacing: 0.3px;
    white-space: nowrap;
  }
  .offer {
    position: absolute; left: 40px; top: 830px;
    display: flex; align-items: center; gap: 10px;
    font-weight: 800; font-size: 27px; color: var(--ink);
    white-space: nowrap;
  }
  .offer-amount {
    background: var(--teal); color: var(--paper);
    padding: 2px 8px; border-radius: 4px; font-size: 27px;
  }
  .fine-print {
    position: absolute; left: 40px; top: 905px; width: 730px;
    display: flex; gap: 12px;
    font-family: "Open Sans", sans-serif; font-size: 9.5px; line-height: 1.45; color: var(--muted);
  }
  .fine-print-label { font-size: 12px; color: var(--ink); white-space: nowrap; padding-top: 10px; }
  .fine-print-body { border-left: 1px solid #bbb; padding-left: 10px; }
  .fine-print-body strong { color: var(--ink); }
  .phone-bar { position: absolute; left: 0; top: 995px; width: 530px; height: 78px; }
  .phone-number {
    position: absolute; left: 78px; top: 1000px;
    font-weight: 700; font-size: 54px; color: var(--paper); letter-spacing: 2px;
    white-space: nowrap;
  }
  .phone-icon { position: absolute; left: 24px; top: 1017px; width: 36px; height: 36px; }
  .contact {
    position: absolute; left: 545px; top: 1010px;
    font-family: "Open Sans", sans-serif; font-size: 12px; color: var(--ink);
    display: flex; flex-direction: column; gap: 12px;
    white-space: nowrap;
  }
  .contact-row { display: flex; align-items: center; gap: 8px; }
  .contact-row svg { width: 13px; height: 13px; flex: none; }
</style>
</head>
<body>
<main class="flyer">
  <div class="brand">
    <span class="brand-mark"></span>
    <span class="brand-name">Harbourleaf Estates Agency</span>
  </div>

  <div class="hero-photo" role="img" aria-label="Photo of modern terraced townhouses with dark balconies, lush gardens and blue sky"></div>

  <svg class="header-stripes" viewBox="0 0 806 240" aria-hidden="true">
    <polygon points="0,178 806,108 806,120 0,190" fill="#4d9ba3"/>
    <polygon points="0,195 806,128 806,134 0,201" fill="#2f7c86"/>
  </svg>

  <svg class="gallery-line" viewBox="0 0 806 260" aria-hidden="true">
    <polygon points="0,210 806,40 806,52 0,222" fill="#4d9ba3"/>
  </svg>

  <div class="thumb thumb--exterior"><div class="thumb-fill" role="img" aria-label="Photo of a contemporary house exterior with pool"></div></div>
  <div class="thumb thumb--living"><div class="thumb-fill" role="img" aria-label="Photo of a bright living and dining room"></div></div>
  <div class="thumb thumb--kitchen"><div class="thumb-fill" role="img" aria-label="Photo of a white kitchen with bar stools"></div></div>

  <h1 class="headline">Invite your friends and receive</h1>
  <p class="offer"><span class="offer-amount">$250</span><span>and they get 2 months free management! *</span></p>

  <div class="fine-print">
    <span class="fine-print-label">Fine Print:</span>
    <p class="fine-print-body">* $250 referral fee paid when the owner you refer signs their property for Management with Harbourleaf Estates Agency. Your referral must be submitted prior to signing on our website using the referral form on this page: <strong>http://www.harbourleafestates.com.au/referral-program/</strong></p>
  </div>

  <svg class="phone-bar" viewBox="0 0 530 78" aria-hidden="true">
    <polygon points="0,0 490,0 470,78 0,78" fill="#4d9ba3"/>
    <polygon points="500,0 520,0 500,78 480,78" fill="#4d9ba3"/>
  </svg>
  <svg class="phone-icon" viewBox="0 0 36 36" aria-hidden="true">
    <path d="M3 12 Q18 2 33 12 L30 17 L24 15 L23 11 Q18 9 13 11 L12 15 L6 17 Z" fill="#fff"/>
    <rect x="8" y="18" width="20" height="14" rx="2" fill="#fff"/>
    <circle cx="18" cy="25" r="3.5" fill="#4d9ba3"/>
  </svg>
  <span class="phone-number">0400 555 217</span>

  <div class="contact">
    <div class="contact-row">
      <svg viewBox="0 0 14 14" aria-hidden="true"><circle cx="7" cy="7" r="6" fill="none" stroke="#4d9ba3" stroke-width="1.5"/><path d="M1 7h12M7 1c-3 3-3 9 0 12M7 1c3 3 3 9 0 12" fill="none" stroke="#4d9ba3" stroke-width="1"/></svg>
      <span>www.harbourleafestates.com.au</span>
    </div>
    <div class="contact-row">
      <svg viewBox="0 0 14 14" aria-hidden="true"><rect x="1" y="3" width="12" height="8" fill="#4d9ba3"/><path d="M1 3l6 5 6-5" fill="none" stroke="#fff" stroke-width="1"/></svg>
      <span>referrals@harbourleafestates.com.au</span>
    </div>
  </div>
</main>
</body>
</html>
```